Young, dynamic furniture company needs a new business card design

We require a new business card design for our modern furniture company which supplies furniture and appliances to the property and development market.
Tallowmere Furnishing has become one of the leading furniture & appliance suppliers to the property market withing London. With over 10 years experience, we have increased our business to supply not only private landlords and managing agents, but also property developers, housing associations and local councils.
We offer not only a complete range of furniture which includes beds, wardrobes, dining sets and sofas, but also a high quality, full delivery and assembly service to help you with all our furnishing needs.

Target Market(s)

Private landlords, estate agents, letting agents, property management companies

Industry/Entity Type

Business

Contact Information for Business Card

Name,
Title,
Address,
Mobile,
Telephone,
Fax, Website, email address

Font styles to use
Sans Serif

Colors
3176b5
0555a3
85abd2
cfdeed

Requirements
Must have
• All the above information for each of our staff, along with our logo

```html
<!DOCTYPE html>
<html lang="en">
<head>
<meta charset="utf-8">
<title>Tallowmere Furnishing – Business Card</title>
<link href="https://fonts.googleapis.com/css2?family=Roboto:wght@300;400;700&display=swap" rel="stylesheet">
<style>
  :root{
    --stage:#1b1b1c;
    --brand-blue:#0555a3;
    --mid-blue:#3176b5;
    --soft-blue:#85abd2;
    --pale-blue:#cfdeed;
    --ink:#1f1f22;
    --grey-ink:#3a3a3e;
    --paper:#ffffff;
    --faint:#e6e8ee;
  }
  *{margin:0;padding:0;box-sizing:border-box}
  html,body{width:1200px;height:923px;overflow:hidden;background:var(--stage);font-family:'Roboto',sans-serif}
  .stage{position:relative;width:1200px;height:923px}
  .card{position:absolute;width:600px;height:343px;border-radius:22px;overflow:hidden}

  /* Back */
  .card-back{left:540px;top:70px;background:linear-gradient(120deg,var(--brand-blue) 0%,var(--mid-blue) 45%,var(--brand-blue) 100%);color:var(--paper)}
  .back-brand{position:absolute;left:0;right:0;top:110px;text-align:center}
  .back-brand .mark{display:inline-flex;align-items:center;gap:12px;font-size:32px;font-weight:300;letter-spacing:1px;text-transform:uppercase}
  .back-brand .mark .dot{width:18px;height:18px;border-radius:50%;background:var(--paper)}
  .back-brand .tagline{margin-top:6px;font-size:12px;font-weight:300;letter-spacing:1.5px;text-transform:uppercase}
  .back-web{position:absolute;left:0;right:0;top:228px;text-align:center;font-size:16px;font-weight:400}

  /* Front */
  .card-front{left:80px;top:470px;background:var(--paper);color:var(--ink)}
  .watermark{position:absolute;right:26px;top:96px;font-size:34px;font-weight:700;line-height:.95;color:var(--faint);text-transform:uppercase;text-align:right}
  .front-brand{position:absolute;left:36px;top:34px}
  .front-brand .mark{display:flex;align-items:center;gap:10px;font-size:26px;font-weight:300;letter-spacing:1px;text-transform:uppercase;color:var(--ink)}
  .front-brand .mark .dot{width:16px;height:16px;border-radius:50%;background:var(--brand-blue)}
  .front-brand .tagline{margin-top:4px;margin-left:26px;font-size:10.5px;letter-spacing:1.3px;text-transform:uppercase;color:var(--grey-ink)}
  .person{position:absolute;left:36px;top:112px;width:290px}
  .person .name{font-size:22px;font-weight:700;color:var(--brand-blue)}
  .person .title-row{display:flex;align-items:flex-end;gap:4px;margin-top:2px}
  .person .title{font-size:15px;color:var(--grey-ink)}
  .person .rule{flex:1;height:1px;margin-bottom:3px;background:linear-gradient(90deg,var(--brand-blue),rgba(5,85,163,0))}
  .address{position:absolute;left:36px;top:184px;font-size:15px;line-height:1.45;color:var(--ink);font-style:normal}
  .contacts{position:absolute;right:30px;bottom:26px;list-style:none;text-align:right}
  .contacts li{display:flex;justify-content:flex-end;align-items:center;gap:10px;font-size:15px;line-height:1.5;color:var(--ink)}
  .contacts .accent{color:var(--brand-blue)}
  .contacts svg{width:15px;height:15px;fill:var(--brand-blue)}
</style>
</head>
<body>
<main class="stage">

  <section class="card card-back" aria-label="Business card back">
    <div class="back-brand">
      <div class="mark"><span class="dot"></span>Tallowmere Furnishing</div>
      <div class="tagline">Trade Furniture Solutions</div>
    </div>
    <div class="back-web">www.tallowmerefurnishing.com</div>
  </section>

  <section class="card card-front" aria-label="Business card front">
    <div class="watermark" aria-hidden="true">Tallowmere<br>Furnishing</div>

    <div class="front-brand">
      <div class="mark"><span class="dot"></span>Tallowmere Furnishing</div>
      <div class="tagline">Trade Furniture Solutions</div>
    </div>

    <div class="person">
      <div class="name">Daniel Reeve</div>
      <div class="title-row"><span class="title">Job Title</span><span class="rule"></span></div>
    </div>

    <address class="address">
      34 Street Name<br>City Name, Country 4567
    </address>

    <ul class="contacts">
      <li>000 1234 5678
        <svg viewBox="0 0 16 16" aria-label="Telephone"><path d="M3 2l3 0 1 3-2 1.5c.8 1.8 2.2 3.2 4 4L10.5 9l3 1v3c0 .6-.5 1-1 1C6.8 14 2 9.2 2 3.5 2 2.5 2.5 2 3 2z"/></svg>
      </li>
      <li>000 1234 5678
        <svg viewBox="0 0 16 16" aria-label="Mobile"><path d="M5 1h6a1 1 0 0 1 1 1v12a1 1 0 0 1-1 1H5a1 1 0 0 1-1-1V2a1 1 0 0 1 1-1zm0 2v9h6V3zm3 10a.8.8 0 1 0 0 1.6A.8.8 0 0 0 8 13z"/></svg>
      </li>
      <li>000 1234 5678
        <svg viewBox="0 0 16 16" aria-label="Fax"><path d="M4 1h6l2 2v3H4zM2 7h12a1 1 0 0 1 1 1v4h-3v3H4v-3H1V8a1 1 0 0 1 1-1zm3 5v2h6v-2z"/></svg>
      </li>
      <li>info@tallowmerefurnishing.com
        <svg viewBox="0 0 16 16" aria-label="Email"><path d="M1 3h14v10H1zm1.5 1.2V5L8 9l5.5-4v-.8L8 8z"/></svg>
      </li>
      <li><span>www.<span class="accent">tallowmerefurnishing</span>.com</span>
        <svg viewBox="0 0 16 16" aria-label="Website"><path d="M8 1a7 7 0 1 0 0 14A7 7 0 0 0 8 1zm0 1.3c.8 0 1.7 1.6 2 3.7H6c.3-2.1 1.2-3.7 2-3.7zM5.8 7h4.4a11 11 0 0 1 0 2H5.8a11 11 0 0 1 0-2zM2.4 7h2.4a12 12 0 0 0 0 2H2.4a5.7 5.7 0 0 1 0-2zm8.8 0h2.4a5.7 5.7 0 0 1 0 2h-2.4a12 12 0 0 0 0-2zM6 10h4c-.3 2.1-1.2 3.7-2 3.7S6.3 12.1 6 10z"/></svg>
      </li>
    </ul>
  </section>

</main>
</body>
</html>
```